Financial Services Company power point theme design

We need a PowerPoint theme designed for client presentations and company orientations. We do like modern designs using blue colors. attached is our logos the logo colors may change as needed to fit the theme. Landscape 16: 9 is acceptable

Industry/Entity Type

Financial Service

Colors

Designer to choose colors to be used in the design.

```html
<!DOCTYPE html>
<html lang="en">
<head>
<meta charset="utf-8">
<title>Keystone Harbor Financial – Presentation Theme</title>
<link href="https://fonts.googleapis.com/css2?family=Lato:wght@300;400;700&display=swap" rel="stylesheet">
<style>
:root{
  --navy:#1d3a6b;
  --navy-2:#25487f;
  --navy-deep:#152c55;
  --steel:#6f87ad;
  --sky:#c3daf0;
  --grey:#8b9098;
  --grey-2:#b3b7bd;
  --light:#eef1f5;
  --ink:#333;
  --white:#fff;
}
*{box-sizing:border-box;margin:0;padding:0}
html,body{width:1200px;height:1200px;overflow:hidden}
body{background:var(--sky);font-family:'Lato',sans-serif;color:var(--ink);position:relative}
.slide{position:absolute;overflow:hidden;background:var(--white);box-shadow:0 1px 3px rgba(20,40,80,.25)}
.slide.dark{background:var(--navy);color:var(--white)}
.slide.pale{background:var(--light)}
.hd{position:absolute;top:5px;left:6px;display:flex;align-items:center;gap:5px;font-size:9px;letter-spacing:.3px;color:var(--navy);text-transform:uppercase;white-space:nowrap}
.dark .hd{color:var(--white)}
.mark{width:9px;height:9px;background:var(--navy);flex:none}
.dark .mark{background:var(--white)}
.hd .rule{width:1px;height:11px;background:currentColor}
.hd.big{font-size:13px;top:6px}
.hd.big .mark{width:12px;height:12px}
.hd.big .rule{height:16px}
.ft{position:absolute;left:0;right:0;bottom:0;height:4px;background:var(--grey-2)}
.url{position:absolute;right:8px;bottom:5px;font-size:3.5px;color:var(--grey)}
.dark .url{color:#c9d4e6}
.t{font-size:3.6px;line-height:1.35;color:#555}
.dark .t,.t.w{color:#dbe3f0}
.t.m{font-size:5px}
.photo{position:absolute}
.ph-city{background:linear-gradient(160deg,#8fa6c6,#3d5d8f 60%,#1d3a6b)}
.ph-glass{background:linear-gradient(135deg,#cfe0f2,#4f79b4 45%,#1b3a70)}
.ph-office{background:linear-gradient(170deg,#f2f4f7,#c7ced8 60%,#6c7787)}
.ph-people{background:linear-gradient(180deg,#e9edf2,#8d96a3 55%,#2e3440)}
.ph-warm{background:linear-gradient(150deg,#d9c4ad,#8c6d55 60%,#3d3a40)}
.ph-rain{background:linear-gradient(160deg,#a9bde0,#4a6fa8 60%,#1d2f55)}
.icon{width:26px;height:26px;border-radius:50%;border:1.5px solid currentColor;display:flex;align-items:center;justify-content:center}
.icon svg{width:13px;height:13px}
.chip{position:absolute;background:var(--navy);color:#fff;font-size:4px;padding:1px 3px}
</style>
</head>
<body>

<!-- 1 Title -->
<section class="slide dark" style="left:12px;top:16px;width:377px;height:212px;background:linear-gradient(180deg,#24477f,#1d3a6b)">
  <div class="photo ph-city" role="img" aria-label="Faint city skyline at dusk" style="inset:0;opacity:.35"></div>
  <div style="position:absolute;left:16px;top:150px;width:62px;height:30px;border:1.5px solid #fff"></div>
  <div style="position:absolute;left:86px;top:148px;font-size:14px;letter-spacing:.4px">KEYSTONE HARBOR FINANCIAL LLC,</div>
  <div style="position:absolute;left:86px;top:168px;font-size:10px">PRESENTATION</div>
  <div style="position:absolute;left:86px;top:192px;font-size:6.5px">www.keystoneharbor.com</div>
</section>

<!-- 8 Services dark -->
<section class="slide dark" style="left:12px;top:240px;width:377px;height:212px">
  <div class="photo ph-city" role="img" aria-label="Business people silhouettes against a skyline" style="inset:0;opacity:.3"></div>
  <div class="hd big"><span class="mark"></span><span class="rule"></span>Our Services</div>
  <div style="position:absolute;left:60px;top:40px;width:270px;display:grid;grid-template-columns:repeat(3,1fr);row-gap:18px;text-align:center;font-size:6px;color:#dbe3f0">
    <div><div class="icon" style="margin:0 auto 6px;width:38px;height:38px;color:#fff"><svg viewBox="0 0 20 20"><text x="10" y="15" text-anchor="middle" font-size="14" fill="#fff" font-family="Lato">$</text></svg></div>Lorem ipsum<br>dolor sit amet</div>
    <div><div class="icon" style="margin:0 auto 6px;width:38px;height:38px;color:#fff"><svg viewBox="0 0 20 20"><rect x="3" y="5" width="14" height="10" fill="none" stroke="#fff" stroke-width="1.5"/></svg></div>Lorem ipsum<br>dolor sit amet</div>
    <div><div class="icon" style="margin:0 auto 6px;width:38px;height:38px;color:#fff"><svg viewBox="0 0 20 20"><path d="M4 16V11M8 16V9M12 16V7M16 16V4" stroke="#fff" stroke-width="2"/></svg></div>Lorem ipsum<br>dolor sit amet</div>
    <div><div class="icon" style="margin:0 auto 6px;width:38px;height:38px;color:#fff"><svg viewBox="0 0 20 20"><rect x="3" y="7" width="14" height="9" fill="#fff"/><rect x="7" y="4" width="6" height="3" fill="none" stroke="#fff"/></svg></div>Lorem ipsum<br>dolor sit amet</div>
    <div><div class="icon" style="margin:0 auto 6px;width:38px;height:38px;color:#fff"><svg viewBox="0 0 20 20"><rect x="5" y="3" width="10" height="14" fill="none" stroke="#fff" stroke-width="1.5"/><path d="M7 7h6M7 10h6M7 13h3" stroke="#fff"/></svg></div>Lorem ipsum<br>dolor sit amet</div>
    <div><div class="icon" style="margin:0 auto 6px;width:38px;height:38px;color:#fff"><svg viewBox="0 0 20 20"><path d="M3 10a7 7 0 0 1 14 0z" fill="#fff"/><path d="M10 10v5a2 2 0 0 1-3 0" stroke="#fff" fill="none"/></svg></div>Lorem ipsum<br>dolor sit amet</div>
  </div>
  <div class="ft"></div><div class="url">www.keystoneharbor.com</div>
</section>

<!-- 2 Cover light -->
<section class="slide pale" style="left:406px;top:20px;width:246px;height:136px">
  <div class="photo ph-office" role="img" aria-label="Faint city skyline" style="inset:0;opacity:.5"></div>
  <div style="position:absolute;right:12px;top:18px;width:70px;height:70px;border:3px solid #b9c4d6"></div>
  <div style="position:absolute;left:10px;top:97px;width:26px;height:14px;background:var(--navy)"></div>
  <div style="position:absolute;left:56px;top:96px;font-size:8px;color:var(--navy)">KEYSTONE HARBOR FINANCIAL LLC,</div>
  <div style="position:absolute;left:56px;top:107px;font-size:6px;color:var(--navy)">PRESENTATION</div>
  <div style="position:absolute;left:56px;top:122px;font-size:3.5px;color:var(--grey)">www.keystoneharbor.com</div>
</section>

<!-- 3 Welcome -->
<section class="slide" style="left:677px;top:20px;width:246px;height:136px">
  <div style="position:absolute;left:0;right:0;top:0;height:72px;background:var(--navy)"></div>
  <div class="mark" style="position:absolute;left:6px;top:5px;background:#fff"></div>
  <div style="position:absolute;left:0;right:0;top:16px;text-align:center;color:#fff;font-size:8px;line-height:1.3">WELCOME<br>MESSAGE</div>
  <div class="photo ph-people" role="img" aria-label="Portrait of the company chairman" style="left:105px;top:48px;width:36px;height:36px"></div>
  <div style="position:absolute;left:40px;top:88px;font-size:14px;color:var(--navy);font-weight:700">&ldquo;</div>
  <p class="t" style="position:absolute;left:62px;top:96px;width:130px;text-align:center">Lorem ipsum dolor sit amet, consectetur adipiscing elit, sed do eiusmod tempor incididunt ut labore et dolore magna aliqua. Ut enim ad minim veniam, quis nostrud exercitation ullamco laboris nisi ut aliquip.</p>
  <div style="position:absolute;left:196px;top:112px;font-size:14px;color:var(--navy);font-weight:700">&rdquo;</div>
  <div class="url" style="font-size:3px">www.keystoneharbor.com &nbsp; 3</div>
</section>

<!-- 4 Quote -->
<section class="slide dark" style="left:942px;top:20px;width:248px;height:138px">
  <div style="position:absolute;left:40px;top:36px;font-size:16px;font-weight:700">&ldquo;</div>
  <p class="t" style="position:absolute;left:64px;top:50px;width:140px;line-height:2.2">Lorem ipsum dolor sit amet, consectetur adipiscing elit, sed do eiusmod tempor incididunt ut labore et dolore magna aliqua. Ut enim ad minim veniam, quis nostrud exercitation ullamco laboris nisi ut aliquip ex ea commodo consequat.</p>
  <div style="position:absolute;left:192px;top:88px;font-size:16px;font-weight:700">&rdquo;</div>
  <div class="url">www.keystoneharbor.com</div>
</section>

<!-- 5 Agenda -->
<section class="slide" style="left:406px;top:170px;width:246px;height:138px">
  <div class="photo ph-office" role="img" aria-label="Laptop on a desk by a window overlooking the city" style="left:0;top:0;width:118px;height:138px"></div>
  <div class="mark" style="position:absolute;left:6px;top:5px"></div>
  <div style="position:absolute;left:118px;top:0;right:0;bottom:0;background:var(--navy);color:#fff">
    <div style="position:absolute;left:8px;top:5px;font-size:8px;border-left:1px solid #fff;padding-left:4px">AGENDA</div>
    <div style="position:absolute;left:10px;top:28px;font-size:8px;line-height:18.5px">01<br>02<br>03<br>04<br>05</div>
    <div style="position:absolute;left:24px;top:30px;width:1px;height:90px;background:#fff"></div>
    <div class="t w" style="position:absolute;left:28px;top:30px;width:96px;line-height:4.6px">
      <p style="height:18.5px">Lorem ipsum dolor sit amet, consectetur adipiscing elit</p>
      <p style="height:18.5px">Lorem ipsum dolor sit amet, consectetur adipiscing elit</p>
      <p style="height:18.5px">Lorem ipsum dolor sit amet, consectetur adipiscing elit</p>
      <p style="height:18.5px">Lorem ipsum dolor sit amet, consectetur adipiscing elit</p>
      <p>Lorem ipsum dolor sit amet, consectetur adipiscing elit</p>
    </div>
    <div class="url">www.keystoneharbor.com</div>
  </div>
</section>

<!-- 6 About us -->
<section class="slide" style="left:677px;top:170px;width:246px;height:138px">
  <div class="hd"><span class="mark"></span><span class="rule"></span>About Us</div>
  <p class="t" style="position:absolute;left:26px;top:30px;width:66px">Lorem ipsum dolor sit amet, consectetur adipiscing elit, sed do eiusmod tempor incididunt ut labore et dolore magna aliqua.<br><br>Ut enim ad minim veniam, quis nostrud exercitation ullamco laboris nisi ut aliquip ex ea commodo consequat.<br><br>Duis aute irure dolor in reprehenderit in voluptate velit esse cillum dolore eu fugiat nulla pariatur.<br><br>Excepteur sint occaecat cupidatat non proident, sunt in culpa qui officia deserunt mollit anim id est laborum.</p>
  <div style="position:absolute;left:95px;top:0;width:62px;height:138px;background:var(--navy);color:#fff;text-align:center;font-size:3.6px">
    <div style="margin-top:22px">&#9670;<br>Lorem ipsum<br>dolor sit amet</div>
    <div style="margin-top:22px">&#9670;<br>Lorem ipsum<br>dolor sit amet</div>
    <div style="margin-top:22px">&#9670;<br>Lorem ipsum<br>dolor sit amet</div>
  </div>
  <div class="photo ph-glass" role="img" aria-label="Glass office tower seen from below" style="left:157px;top:0;right:0;bottom:0"></div>
  <div class="url" style="color:#fff">www.keystoneharbor.com</div>
</section>

<!-- 7 About us 2 -->
<section class="slide" style="left:942px;top:170px;width:248px;height:136px">
  <div class="hd"><span class="mark"></span><span class="rule"></span>About Us</div>
  <p class="t" style="position:absolute;left:26px;top:25px;width:120px">Lorem ipsum dolor sit amet, consectetur adipiscing elit, sed do eiusmod tempor incididunt ut labore et dolore magna aliqua.<br>Ut enim ad minim veniam, quis nostrud exercitation ullamco laboris nisi ut aliquip ex ea commodo consequat.<br>Duis aute irure dolor in reprehenderit in voluptate velit esse cillum dolore eu fugiat nulla pariatur.<br>Excepteur sint occaecat cupidatat non proident, sunt in culpa qui officia deserunt mollit anim id est laborum.</p>
  <div class="t" style="position:absolute;left:24px;top:92px;width:120px;display:flex;justify-content:space-between;text-align:center;color:var(--navy)">
    <span>&#9670;<br>Lorem ipsum<br>dolor sit amet</span><span>&#9670;<br>Lorem ipsum<br>dolor sit amet</span><span>&#9670;<br>Lorem ipsum<br>dolor sit amet</span>
  </div>
  <div class="photo ph-glass" role="img" aria-label="Glass office tower seen from below" style="left:156px;top:0;right:0;bottom:0"></div>
  <div class="url" style="color:#fff">www.keystoneharbor.com</div>
</section>

<!-- 9 Services light -->
<section class="slide" style="left:406px;top:318px;width:246px;height:138px;background:linear-gradient(180deg,#fff,#e4e8ee)">
  <div class="hd"><span class="mark"></span><span class="rule"></span>Our Services</div>
  <div style="position:absolute;left:30px;top:26px;width:190px;display:grid;grid-template-columns:repeat(3,1fr);row-gap:8px;text-align:center;font-size:3.6px;color:var(--grey);justify-items:center">
    <div><div class="icon" style="color:var(--navy);margin-bottom:2px"><svg viewBox="0 0 20 20"><text x="10" y="15" text-anchor="middle" font-size="13" fill="#1d3a6b" font-family="Lato">$</text></svg></div>Lorem ipsum<br>dolor sit amet</div>
    <div><div class="icon" style="color:var(--navy);margin-bottom:2px"><svg viewBox="0 0 20 20"><rect x="3" y="5" width="14" height="10" fill="none" stroke="#1d3a6b" stroke-width="1.5"/></svg></div>Lorem ipsum<br>dolor sit amet</div>
    <div><div class="icon" style="color:var(--navy);margin-bottom:2px"><svg viewBox="0 0 20 20"><path d="M4 16V11M8 16V9M12 16V7M16 16V4" stroke="#1d3a6b" stroke-width="2"/></svg></div>Lorem ipsum<br>dolor sit amet</div>
    <div><div class="icon" style="color:var(--navy);margin-bottom:2px"><svg viewBox="0 0 20 20"><rect x="3" y="7" width="14" height="9" fill="#1d3a6b"/></svg></div>Lorem ipsum<br>dolor sit amet</div>
    <div><div class="icon" style="color:var(--navy);margin-bottom:2px"><svg viewBox="0 0 20 20"><rect x="5" y="3" width="10" height="14" fill="none" stroke="#1d3a6b" stroke-width="1.5"/></svg></div>Lorem ipsum<br>dolor sit amet</div>
    <div><div class="icon" style="color:var(--navy);margin-bottom:2px"><svg viewBox="0 0 20 20"><path d="M3 10a7 7 0 0 1 14 0z" fill="#1d3a6b"/></svg></div>Lorem ipsum<br>dolor sit amet</div>
  </div>
  <div class="ft"></div><div class="url">www.keystoneharbor.com</div>
</section>

<!-- 10 Team photo -->
<section class="slide" style="left:677px;top:318px;width:246px;height:138px">
  <div class="photo ph-people" role="img" aria-label="Group of business professionals in suits" style="left:100px;top:0;right:0;height:88px"></div>
  <div style="position:absolute;left:22px;top:0;width:78px;height:86px;background:var(--navy)"></div>
  <div class="mark" style="position:absolute;left:6px;top:5px"></div>
  <p class="t w" style="position:absolute;left:27px;top:20px;width:68px">Lorem ipsum dolor sit amet, consectetur adipiscing elit, sed do eiusmod tempor incididunt ut labore et dolore magna aliqua. Ut enim ad minim veniam, quis nostrud exercitation ullamco laboris nisi ut aliquip ex ea commodo consequat.</p>
  <div style="position:absolute;left:0;right:0;top:90px;display:flex;justify-content:space-around;text-align:center;color:var(--navy);font-size:6px">
    <div>Lorem ipsum<br>dolor sit amet<p class="t" style="width:60px">Lorem ipsum dolor sit amet, consectetur adipiscing elit sed do eiusmod.</p></div>
    <div>Lorem ipsum<br>dolor sit amet<p class="t" style="width:60px">Lorem ipsum dolor sit amet, consectetur adipiscing elit sed do eiusmod.</p></div>
    <div>Lorem ipsum<br>dolor sit amet<p class="t" style="width:60px">Lorem ipsum dolor sit amet, consectetur adipiscing elit sed do eiusmod.</p></div>
  </div>
</section>

<!-- 11 Unique approach -->
<section class="slide pale" style="left:942px;top:318px;width:248px;height:138px">
  <div class="mark" style="position:absolute;left:6px;top:5px"></div>
  <div style="position:absolute;left:28px;top:0;width:78px;height:130px;background:var(--navy);color:#fff;padding:12px 6px">
    <div style="font-size:5px">OUR UNIQUE</div>
    <div style="font-size:8px;margin-bottom:3px">APPROACH</div>
    <p class="t w" style="font-size:3.2px">Our client's goals, objectives and dreams, and concerns come first. We listen, evaluate or help you identify both your short- and long-term goals and help you make informed decisions about every aspect of your financial life. Whether it's taking out a new mortgage, saving for your children's college or as a business owner, establishing benefits for your employees, our team of experts will guide you through all the moving pieces.</p>
  </div>
  <div class="photo ph-office" role="img" aria-label="Faint office interior" style="left:106px;top:0;right:0;bottom:0;opacity:.5"></div>
  <div style="position:absolute;left:122px;top:10px;width:118px;font-size:5px;color:var(--navy)">
    <div style="display:flex;gap:6px;margin-bottom:14px"><span class="icon" style="width:18px;height:18px;background:var(--navy);flex:none"></span><div>OUR MISSION<p class="t" style="font-size:3.2px">Our mission is to educate and help guide our clients through these important stages.</p></div></div>
    <div style="display:flex;gap:6px;margin-bottom:14px"><span class="icon" style="width:18px;height:18px;background:var(--navy);flex:none"></span><div>OUR VALUE<p class="t" style="font-size:3.2px">Our value to our clients is being your go-to resource for any financial questions.</p></div></div>
    <div style="display:flex;gap:6px"><span class="icon" style="width:18px;height:18px;background:var(--navy);flex:none"></span><div>OUR EXPERTISE<p class="t" style="font-size:3.2px">Each of the advisors in our office brings a different area of expertise to provide a wide-ranging approach.</p></div></div>
  </div>
</section>

<!-- Row 4 -->
<section class="slide" style="left:12px;top:466px;width:226px;height:126px">
  <div style="position:absolute;left:0;top:0;width:50px;height:126px;background:var(--navy);color:#fff;font-size:7px;text-align:center;padding-top:50px;line-height:1.3">MEET<br>OUR<br>CEO</div>
  <div class="mark" style="position:absolute;left:6px;top:5px;background:#fff"></div>
  <div class="photo ph-people" role="img" aria-label="Portrait of the chief executive officer" style="left:50px;top:0;width:78px;height:126px;background:linear-gradient(180deg,#3a3a3a,#111)"></div>
  <div style="position:absolute;left:136px;top:12px;font-size:4.5px;color:#444">Name</div>
  <p class="t" style="position:absolute;left:136px;top:20px;width:82px">Lorem ipsum dolor sit amet, consectetur adipiscing elit, sed do eiusmod tempor incididunt ut labore et dolore magna aliqua.<br>Ut enim ad minim veniam, quis nostrud exercitation ullamco laboris nisi ut aliquip ex ea commodo consequat.<br>Duis aute irure dolor in reprehenderit in voluptate velit esse cillum dolore eu fugiat nulla pariatur.</p>
  <div style="position:absolute;left:140px;top:98px;display:flex;gap:24px"><span class="mark"></span><span class="mark"></span><span class="mark"></span></div>
</section>

<section class="slide" style="left:250px;top:466px;width:224px;height:126px">
  <div class="hd"><span class="mark"></span><span class="rule"></span>Meet Our Team</div>
  <div style="position:absolute;left:12px;top:24px;right:12px;display:flex;justify-content:space-between;text-align:center;font-size:4.5px;color:#444">
    <div><div class="ph-people" role="img" aria-label="Team member portrait" style="width:40px;height:62px;margin-bottom:4px"></div>Name<br>Position</div>
    <div><div class="ph-warm" role="img" aria-label="Team member portrait" style="width:40px;height:62px;margin-bottom:4px"></div>Name<br>Position</div>
    <div><div class="ph-people" role="img" aria-label="Team member portrait" style="width:40px;height:62px;margin-bottom:4px"></div>Name<br>Position</div>
    <div><div class="ph-warm" role="img" aria-label="Team member portrait" style="width:40px;height:62px;margin-bottom:4px"></div>Name<br>Position</div>
  </div>
  <div class="ft"></div><div class="url">www.keystoneharbor.com</div>
</section>

<section class="slide" style="left:486px;top:466px;width:226px;height:126px">
  <div class="hd"><span class="mark"></span><span class="rule"></span>Meet Our Team</div>
  <div style="position:absolute;left:26px;top:22px;width:180px;display:grid;grid-template-columns:repeat(4,1fr);row-gap:4px;text-align:center;font-size:4px;color:#444;justify-items:center">
    <div><div class="ph-people" role="img" aria-label="Team member portrait" style="width:28px;height:30px"></div>Name<br>Position</div>
    <div><div class="ph-warm" role="img" aria-label="Team member portrait" style="width:28px;height:30px"></div>Name<br>Position</div>
    <div><div class="ph-people" role="img" aria-label="Team member portrait" style="width:28px;height:30px"></div>Name<br>Position</div>
    <div><div class="ph-warm" role="img" aria-label="Team member portrait" style="width:28px;height:30px"></div>Name<br>Position</div>
    <div><div class="ph-people" role="img" aria-label="Team member portrait" style="width:28px;height:30px"></div>Name<br>Position</div>
    <div><div class="ph-warm" role="img" aria-label="Team member portrait" style="width:28px;height:30px"></div>Name<br>Position</div>
    <div><div class="ph-people" role="img" aria-label="Team member portrait" style="width:28px;height:30px"></div>Name<br>Position</div>
    <div><div class="ph-warm" role="img" aria-label="Team member portrait" style="width:28px;height:30px"></div>Name<br>Position</div>
  </div>
  <div class="ft"></div><div class="url">www.keystoneharbor.com</div>
</section>

<section class="slide" style="left:722px;top:466px;width:226px;height:126px">
  <div class="hd"><span class="mark"></span><span class="rule"></span>Column Text</div>
  <div class="chip" style="left:24px;top:24px;width:84px">Lorem ipsum dolor sit amet</div>
  <div class="chip" style="left:122px;top:24px;width:84px">Lorem ipsum dolor sit amet</div>
  <p class="t" style="position:absolute;left:24px;top:36px;width:84px">Lorem ipsum dolor sit amet, consectetur adipiscing elit, sed do eiusmod tempor incididunt ut labore et dolore magna aliqua.<br><br>Ut enim ad minim veniam, quis nostrud exercitation ullamco laboris nisi ut aliquip ex ea commodo consequat.<br><br>Duis aute irure dolor in reprehenderit in voluptate velit esse cillum dolore eu fugiat nulla pariatur.<br><br>Excepteur sint occaecat cupidatat non proident, sunt in culpa qui officia deserunt mollit anim id est laborum.</p>
  <p class="t" style="position:absolute;left:122px;top:36px;width:84px">Lorem ipsum dolor sit amet, consectetur adipiscing elit, sed do eiusmod tempor incididunt ut labore et dolore magna aliqua.<br><br>Ut enim ad minim veniam, quis nostrud exercitation ullamco laboris nisi ut aliquip ex ea commodo consequat.<br><br>Duis aute irure dolor in reprehenderit in voluptate velit esse cillum dolore eu fugiat nulla pariatur.<br><br>Excepteur sint occaecat cupidatat non proident, sunt in culpa qui officia deserunt mollit anim id est laborum.</p>
  <div class="ft"></div><div class="url">www.keystoneharbor.com</div>
</section>

<section class="slide" style="left:960px;top:466px;width:230px;height:126px">
  <div class="hd"><span class="mark"></span><span class="rule"></span>Column Text</div>
  <div style="position:absolute;left:12px;top:22px;width:70px;height:96px;background:var(--navy);color:#fff;font-size:5px;padding:3px;line-height:1.3">Lorem ipsum dolor sit amet, consectetur adipiscing elit, sed do eiusmod tempor incididunt ut labore et dolore magna aliqua. Ut enim ad minim veniam, quis nostrud exercitation ullamco laboris nisi ut aliquip ex ea commodo consequat.</div>
  <div class="chip" style="left:88px;top:24px;width:64px">Lorem ipsum dolor sit amet</div>
  <div class="chip" style="left:158px;top:24px;width:64px">Lorem ipsum dolor sit amet</div>
  <p class="t" style="position:absolute;left:88px;top:36px;width:64px">Lorem ipsum dolor sit amet, consectetur adipiscing elit, sed do eiusmod tempor incididunt ut labore et dolore magna aliqua. Ut enim ad minim veniam, quis nostrud exercitation ullamco laboris. Duis aute irure dolor in reprehenderit in voluptate velit esse cillum dolore eu fugiat nulla pariatur.</p>
  <p class="t" style="position:absolute;left:158px;top:36px;width:64px">Lorem ipsum dolor sit amet, consectetur adipiscing elit, sed do eiusmod tempor incididunt ut labore et dolore magna aliqua. Ut enim ad minim veniam, quis nostrud exercitation ullamco laboris. Duis aute irure dolor in reprehenderit in voluptate velit esse cillum dolore eu fugiat nulla pariatur.</p>
  <div class="ft"></div><div class="url">www.keystoneharbor.com</div>
</section>

<!-- Row 5 -->
<section class="slide" style="left:12px;top:602px;width:226px;height:126px">
  <div class="hd"><span class="mark"></span><span class="rule"></span>Column Text</div>
  <div style="position:absolute;left:22px;top:24px;width:184px;background:var(--navy);color:#fff;font-size:5.5px;padding:2px 3px;line-height:1.3">Lorem ipsum dolor sit amet, consectetur adipiscing elit, sed do eiusmod tempor incididunt ut labore et dolore magna aliqua.</div>
  <p class="t" style="position:absolute;left:22px;top:50px;width:86px">Lorem ipsum dolor sit amet, consectetur adipiscing elit, sed do eiusmod tempor incididunt ut labore et dolore magna aliqua.<br><br>Ut enim ad minim veniam, quis nostrud exercitation ullamco laboris nisi ut aliquip ex ea commodo consequat.<br><br>Duis aute irure dolor in reprehenderit in voluptate velit esse cillum dolore eu fugiat nulla pariatur.</p>
  <p class="t" style="position:absolute;left:120px;top:50px;width:86px">Lorem ipsum dolor sit amet, consectetur adipiscing elit, sed do eiusmod tempor incididunt ut labore et dolore magna aliqua.<br><br>Ut enim ad minim veniam, quis nostrud exercitation ullamco laboris nisi ut aliquip ex ea commodo consequat.<br><br>Duis aute irure dolor in reprehenderit in voluptate velit esse cillum dolore eu fugiat nulla pariatur.</p>
  <div class="ft"></div><div class="url">www.keystoneharbor.com</div>
</section>

<section class="slide dark" style="left:250px;top:602px;width:224px;height:126px">
  <div class="hd"><span class="mark"></span><span class="rule"></span>Timeline History</div>
  <svg style="position:absolute;left:0;top:0" width="224" height="126">
    <line x1="10" y1="64" x2="214" y2="64" stroke="#fff" stroke-width=".8"/>
    <g fill="#fff"><circle cx="45" cy="64" r="1.6"/><circle cx="78" cy="64" r="1.6"/><circle cx="111" cy="64" r="1.6"/><circle cx="144" cy="64" r="1.6"/><circle cx="180" cy="64" r="1.6"/></g>
    <g stroke="#fff" stroke-width=".4"><line x1="45" y1="28" x2="45" y2="64"/><line x1="111" y1="28" x2="111" y2="64"/><line x1="180" y1="28" x2="180" y2="64"/><line x1="78" y1="64" x2="78" y2="100"/><line x1="144" y1="64" x2="144" y2="100"/></g>
  </svg>
  <div style="position:absolute;left:64px;top:54px;font-size:7px">2015</div>
  <div style="position:absolute;left:140px;top:54px;font-size:7px">2017</div>
  <div style="position:absolute;left:36px;top:70px;font-size:7px">2014</div>
  <div style="position:absolute;left:103px;top:70px;font-size:7px">2016</div>
  <div style="position:absolute;left:172px;top:70px;font-size:7px">2018</div>
  <p class="t" style="position:absolute;left:46px;top:28px;width:30px;font-size:2.8px">Lorem ipsum dolor sit amet, consectetur adipiscing elit, sed do eiusmod tempor incididunt ut labore.</p>
  <p class="t" style="position:absolute;left:112px;top:28px;width:30px;font-size:2.8px">Lorem ipsum dolor sit amet, consectetur adipiscing elit, sed do eiusmod tempor incididunt ut labore.</p>
  <p class="t" style="position:absolute;left:181px;top:28px;width:30px;font-size:2.8px">Lorem ipsum dolor sit amet, consectetur adipiscing elit, sed do eiusmod tempor incididunt ut labore.</p>
  <p class="t" style="position:absolute;left:79px;top:84px;width:30px;font-size:2.8px">Lorem ipsum dolor sit amet, consectetur adipiscing elit, sed do eiusmod tempor incididunt ut labore.</p>
  <p class="t" style="position:absolute;left:145px;top:84px;width:30px;font-size:2.8px">Lorem ipsum dolor sit amet, consectetur adipiscing elit, sed do eiusmod tempor incididunt ut labore.</p>
  <div class="url">www.keystoneharbor.com</div>
</section>

<section class="slide" style="left:486px;top:602px;width:226px;height:126px">
  <div class="hd"><span class="mark"></span><span class="rule"></span><span style="text-transform:none">WHY CHOOSE US? (editable chart)</span></div>
  <p class="t" style="position:absolute;left:26px;top:18px;width:150px">Lorem ipsum dolor sit amet, consectetur adipiscing elit, sed do eiusmod tempor incididunt ut labore et dolore magna aliqua.<br>Ut enim ad minim veniam, quis nostrud exercitation ullamco laboris nisi ut aliquip ex ea commodo consequat.</p>
  <div style="position:absolute;left:0;right:0;top:44px;height:62px;background:var(--navy)"></div>
  <svg style="position:absolute;left:0;top:44px" width="226" height="62">
    <g fill="none" stroke-width="3.5">
      <circle cx="41" cy="31" r="12" stroke="#5a78a8"/><circle cx="41" cy="31" r="12" stroke="#fff" stroke-dasharray="71.6 75.4" transform="rotate(-90 41 31)"/>
      <circle cx="91" cy="31" r="12" stroke="#5a78a8"/><circle cx="91" cy="31" r="12" stroke="#fff" stroke-dasharray="68.6 75.4" transform="rotate(-90 91 31)"/>
      <circle cx="141" cy="31" r="12" stroke="#5a78a8"/><circle cx="141" cy="31" r="12" stroke="#fff" stroke-dasharray="70.1 75.4" transform="rotate(-90 141 31)"/>
      <circle cx="191" cy="31" r="12" stroke="#5a78a8"/><circle cx="191" cy="31" r="12" stroke="#fff" stroke-dasharray="67.1 75.4" transform="rotate(-90 191 31)"/>
    </g>
    <g fill="#fff" font-size="7" font-family="Lato" text-anchor="middle"><text x="41" y="34">95%</text><text x="91" y="34">91%</text><text x="141" y="34">93%</text><text x="191" y="34">89%</text></g>
    <g fill="#fff" font-size="3.2" font-family="Lato" text-anchor="middle"><text x="41" y="51">CASH FLOW</text><text x="41" y="55">ANALYSIS</text><text x="91" y="51">RETIREMENT</text><text x="91" y="55">PLANNING</text><text x="141" y="51">INSURANCE</text><text x="141" y="55">PLANNING</text><text x="191" y="51">ASSET</text><text x="191" y="55">ALLOCATION</text></g>
  </svg>
  <div class="ft"></div><div class="url">www.keystoneharbor.com</div>
</section>

<section class="slide" style="left:722px;top:602px;width:226px;height:126px">
  <div class="hd"><span class="mark"></span><span class="rule"></span>Editable Chart</div>
  <svg style="position:absolute;left:24px;top:22px" width="132" height="90">
    <rect width="132" height="84" fill="#e8ebef"/>
    <g font-family="Lato" font-size="3.2" fill="#555"><text x="4" y="12">CASH FLOW ANALYSIS</text><text x="4" y="31">RETIREMENT PLANNING</text><text x="4" y="50">INSURANCE PLANNING</text><text x="10" y="69">ASSET ALLOCATION</text></g>
    <rect x="56" y="6" width="72" height="10" fill="#1d3a6b"/><rect x="56" y="25" width="52" height="10" fill="#1d3a6b"/><rect x="56" y="44" width="62" height="10" fill="#1d3a6b"/><rect x="56" y="63" width="20" height="10" fill="#1d3a6b"/>
    <g font-family="Lato" font-size="5" fill="#fff" text-anchor="end"><text x="126" y="13">95%</text><text x="106" y="32">91%</text><text x="116" y="51">93%</text><text x="74" y="70">89%</text></g>
    <g font-family="Lato" font-size="3" fill="#777"><text x="54" y="89">86</text><text x="68" y="89">88</text><text x="82" y="89">90</text><text x="96" y="89">92</text><text x="110" y="89">94</text><text x="124" y="89">96</text></g>
  </svg>
  <div style="position:absolute;left:166px;top:24px;font-size:5.5px;color:#333">INFORMATION</div>
  <p class="t" style="position:absolute;left:166px;top:34px;width:52px">Lorem ipsum dolor sit amet, consectetur adipiscing elit, sed do eiusmod tempor incididunt ut labore et dolore magna aliqua. Ut enim ad minim veniam, quis nostrud exercitation ullamco laboris nisi ut aliquip. Duis aute irure dolor in reprehenderit in voluptate velit esse cillum dolore eu fugiat nulla pariatur.</p>
  <div class="ft"></div><div class="url">www.keystoneharbor.com</div>
</section>

<section class="slide" style="left:960px;top:602px;width:230px;height:126px">
  <div class="hd"><span class="mark"></span><span class="rule"></span>Editable Chart</div>
  <svg style="position:absolute;left:24px;top:24px" width="130" height="90">
    <rect width="130" height="86" fill="#e8ebef"/>
    <g stroke="#d0d5dc" stroke-width=".4"><line x1="10" y1="14" x2="128" y2="14"/><line x1="10" y1="28" x2="128" y2="28"/><line x1="10" y1="42" x2="128" y2="42"/><line x1="10" y1="56" x2="128" y2="56"/><line x1="10" y1="70" x2="128" y2="70"/></g>
    <defs><linearGradient id="barFade" x1="0" y1="0" x2="0" y2="1"><stop offset="0" stop-color="#1d3a6b"/><stop offset="1" stop-color="#e8ebef"/></linearGradient></defs>
    <rect x="16" y="64" width="18" height="14" fill="url(#barFade)"/><rect x="44" y="32" width="18" height="46" fill="url(#barFade)"/><rect x="74" y="48" width="18" height="30" fill="url(#barFade)"/><rect x="104" y="16" width="18" height="62" fill="url(#barFade)"/>
    <g font-family="Lato" font-size="5" fill="#1d3a6b" text-anchor="middle"><text x="25" y="62">89%</text><text x="53" y="30">93%</text><text x="83" y="46">91%</text><text x="113" y="14">95%</text></g>
    <g font-family="Lato" font-size="2.6" fill="#555" text-anchor="middle"><text x="25" y="83">ASSET</text><text x="53" y="83">INSURANCE</text><text x="83" y="83">RETIREMENT</text><text x="113" y="83">CASH FLOW</text></g>
  </svg>
  <div style="position:absolute;left:164px;top:30px;font-size:5.5px;color:#333">INFORMATION</div>
  <p class="t" style="position:absolute;left:164px;top:40px;width:56px">Lorem ipsum dolor sit amet, consectetur adipiscing elit, sed do eiusmod tempor incididunt ut labore et dolore magna aliqua. Ut enim ad minim veniam, quis nostrud exercitation ullamco laboris nisi ut aliquip. Duis aute irure dolor in reprehenderit in voluptate velit.</p>
  <div class="ft"></div><div class="url">www.keystoneharbor.com</div>
</section>

<!-- Row 6 -->
<section class="slide" style="left:6px;top:740px;width:290px;height:164px">
  <div class="hd big"><span class="mark"></span><span class="rule"></span>Chart Style</div>
  <svg style="position:absolute;left:0;top:0" width="290" height="164">
    <g transform="translate(0 22)">
      <path d="M50 96 C64 96 68 20 92 20 C114 20 118 96 132 96Z" fill="#1d3a6b"/>
      <path d="M90 96 C104 96 110 38 128 38 C146 38 152 96 166 96Z" fill="#8b9098"/>
      <path d="M124 96 C138 96 146 30 162 30 C180 30 188 96 200 96Z" fill="#2d5596" opacity=".95"/>
      <path d="M160 96 C176 96 184 48 202 48 C220 48 226 96 240 96Z" fill="#b3b7bd"/>
      <g font-family="Lato" font-size="10" font-weight="700"><text x="83" y="16" fill="#1d3a6b">95%</text><text x="119" y="34" fill="#8b9098">91%</text><text x="153" y="26" fill="#2d5596">93%</text><text x="192" y="44" fill="#b3b7bd">89%</text></g>
      <circle cx="76" cy="112" r="5" fill="#1d3a6b"/><circle cx="76" cy="127" r="5" fill="#8b9098"/><circle cx="162" cy="112" r="5" fill="#2d5596"/><circle cx="162" cy="127" r="5" fill="#b3b7bd"/>
      <g font-family="Lato" font-size="5" fill="#333"><text x="86" y="114">CASH FLOW ANALYSIS</text><text x="86" y="129">RETIREMENT PLANNING</text><text x="172" y="114">INSURANCE PLANNING</text><text x="172" y="129">ASSET ALLOCATION</text></g>
    </g>
  </svg>
  <div class="ft"></div><div class="url">www.keystoneharbor.com</div>
</section>

<section class="slide" style="left:306px;top:740px;width:290px;height:164px">
  <div class="hd big"><span class="mark"></span><span class="rule"></span>Lorem Ipsum</div>
  <p class="t" style="position:absolute;left:32px;top:28px;width:100px;font-size:4.2px">Lorem ipsum dolor sit amet, consectetur adipiscing elit, sed do eiusmod tempor incididunt ut labore et dolore magna aliqua.<br>Ut enim ad minim veniam, quis nostrud exercitation ullamco laboris nisi ut aliquip ex ea commodo consequat.</p>
  <div class="t" style="position:absolute;left:34px;top:72px;width:80px;font-size:4.2px;line-height:1.3">
    <p style="border-left:3px solid var(--navy);padding-left:4px;margin-bottom:8px">Lorem ipsum dolor sit amet, consectetur adipiscing elit.</p>
    <p style="border-left:3px solid var(--navy);padding-left:4px;margin-bottom:8px">Lorem ipsum dolor sit amet, consectetur adipiscing elit.</p>
    <p style="border-left:3px solid var(--grey);padding-left:4px">Lorem ipsum dolor sit amet, consectetur adipiscing elit.</p>
  </div>
  <svg style="position:absolute;left:136px;top:20px" width="150" height="140">
    <circle cx="76" cy="44" r="38" fill="#1d3a6b"/>
    <circle cx="54" cy="88" r="38" fill="#8b9098" opacity=".85"/>
    <circle cx="98" cy="88" r="38" fill="#2d5596" opacity=".85"/>
    <g font-family="Lato" font-size="5" fill="#fff" text-anchor="middle"><text x="76" y="32">LOREM</text><text x="76" y="38">IPSUM</text><text x="36" y="96">LOREM</text><text x="36" y="102">IPSUM</text><text x="116" y="96">LOREM</text><text x="116" y="102">IPSUM</text></g>
  </svg>
  <div class="ft"></div><div class="url">www.keystoneharbor.com</div>
</section>

<section class="slide" style="left:606px;top:740px;width:290px;height:164px">
  <div class="hd big"><span class="mark"></span><span class="rule"></span>Lorem Ipsum</div>
  <svg style="position:absolute;left:20px;top:28px" width="130" height="124">
    <path d="M10 4h34l14 16-14 16H24v20H10z" fill="#1d3a6b"/>
    <path d="M70 6h48v36H96L84 56 70 42z" fill="#b3b7bd"/>
    <path d="M62 72h16v40H44L30 96l14-16h18z" fill="#1d3a6b" transform="translate(20 0)"/>
    <path d="M24 68l18 16H34v32H14V84H6z" fill="#b3b7bd"/>
    <g font-family="Lato" font-size="4.5" fill="#fff"><text x="80" y="20">Lorem Ipsum</text></g>
    <g font-family="Lato" font-size="4.5" fill="#555"><text x="14" y="122">Lorem Ipsum</text></g>
  </svg>
  <div class="t" style="position:absolute;left:160px;top:34px;width:118px;font-size:3.6px">
    <p style="color:var(--navy);font-size:5px">Lorem Ipsum</p><p style="margin-bottom:8px">Lorem ipsum dolor sit amet, consectetur adipiscing elit, sed do eiusmod tempor incididunt ut labore et dolore magna aliqua.</p>
    <p style="color:var(--grey);font-size:5px">Lorem Ipsum</p><p style="margin-bottom:8px">Lorem ipsum dolor sit amet, consectetur adipiscing elit, sed do eiusmod tempor incididunt ut labore et dolore magna aliqua.</p>
    <p style="color:var(--navy);font-size:5px">Lorem Ipsum</p><p style="margin-bottom:8px">Lorem ipsum dolor sit amet, consectetur adipiscing elit, sed do eiusmod tempor incididunt ut labore et dolore magna aliqua.</p>
    <p style="color:var(--grey);font-size:5px">Lorem Ipsum</p><p>Lorem ipsum dolor sit amet, consectetur adipiscing elit, sed do eiusmod tempor incididunt ut labore et dolore magna aliqua.</p>
  </div>
  <div class="ft"></div><div class="url">www.keystoneharbor.com</div>
</section>

<section class="slide" style="left:904px;top:740px;width:290px;height:164px">
  <div class="hd big"><span class="mark"></span><span class="rule"></span>Table List</div>
  <p class="t" style="position:absolute;left:36px;top:26px;width:220px;font-size:4.4px">Lorem ipsum dolor sit amet, consectetur adipiscing elit, sed do eiusmod tempor incididunt ut labore et dolore magna aliqua.</p>
  <table style="position:absolute;left:34px;top:48px;width:230px;border-collapse:collapse;font-size:4px;text-align:center;color:#555">
    <tr style="background:#c9cdd3;height:20px"><td></td><td>Text</td><td>Text</td><td>Text</td><td>Text</td><td>Text</td></tr>
    <tr style="background:#a9c3e6;height:20px"><td style="background:var(--navy-2);color:#fff">Add Text</td><td>Text</td><td>Text</td><td>Text</td><td>Text</td><td>Text</td></tr>
    <tr style="background:#e8ebef;height:20px"><td style="background:#55595f;color:#fff">Add Text</td><td>Text</td><td>Text</td><td>Text</td><td>Text</td><td>Text</td></tr>
  </table>
  <div style="position:absolute;left:34px;top:124px;width:230px;background:#55595f;color:#fff;font-size:4.4px;text-align:center;padding:2px">Lorem ipsum dolor sit amet, consectetur adipiscing elit, sed do eiusmod tempor incididunt ut labore et dolore magna aliqua.</div>
  <div class="ft"></div><div class="url">www.keystoneharbor.com</div>
</section>

<!-- Row 7 -->
<section class="slide" style="left:12px;top:918px;width:226px;height:126px">
  <div class="photo ph-office" role="img" aria-label="Faint bright office interior" style="inset:0;opacity:.5"></div>
  <div class="hd"><span class="mark"></span><span class="rule"></span>Lorem Ipsum</div>
  <p class="t" style="position:absolute;left:34px;top:22px;width:160px">Lorem ipsum dolor sit amet, consectetur adipiscing elit, sed do eiusmod tempor incididunt ut labore et dolore magna aliqua.<br>Ut enim ad minim veniam, quis nostrud exercitation ullamco laboris nisi ut aliquip ex ea commodo consequat.</p>
  <div style="position:absolute;left:26px;top:56px;width:180px;display:grid;grid-template-columns:1fr 1fr;row-gap:16px;font-size:3.6px;color:#444">
    <div style="display:flex;gap:3px"><b style="font-size:11px;color:var(--navy);border-right:1px solid var(--navy);padding-right:3px">1</b><span>Lorem ipsum dolor sit amet,<br>consectetur adipiscing elit</span></div>
    <div style="display:flex;gap:3px"><b style="font-size:11px;color:var(--navy);border-right:1px solid var(--navy);padding-right:3px">3</b><span>Lorem ipsum dolor sit amet,<br>consectetur adipiscing elit</span></div>
    <div style="display:flex;gap:3px"><b style="font-size:11px;color:var(--navy);border-right:1px solid var(--navy);padding-right:3px">2</b><span>Lorem ipsum dolor sit amet,<br>consectetur adipiscing elit</span></div>
    <div style="display:flex;gap:3px"><b style="font-size:11px;color:var(--navy);border-right:1px solid var(--navy);padding-right:3px">4</b><span>Lorem ipsum dolor sit amet,<br>consectetur adipiscing elit</span></div>
  </div>
  <div class="ft"></div><div class="url">www.keystoneharbor.com</div>
</section>

<section class="slide" style="left:250px;top:918px;width:224px;height:126px">
  <div class="hd"><span class="mark"></span><span class="rule"></span>Lorem Ipsum</div>
  <div class="photo ph-warm" role="img" aria-label="Hands reviewing financial documents at a desk" style="left:22px;top:22px;width:80px;height:80px"></div>
  <div style="position:absolute;left:40px;top:26px;width:32px;height:70px;background:var(--navy);opacity:.9"></div>
  <p class="t w" style="position:absolute;left:42px;top:44px;width:28px;font-size:3.4px">Lorem ipsum dolor sit amet, consectetur adipiscing elit</p>
  <div style="position:absolute;left:88px;top:26px;width:14px;height:70px;background:var(--navy);display:flex;flex-direction:column;justify-content:space-around;align-items:center"><span class="mark" style="background:#fff;width:6px;height:6px"></span><span class="mark" style="background:#fff;width:6px;height:6px"></span><span class="mark" style="background:#fff;width:6px;height:6px"></span></div>
  <p class="t" style="position:absolute;left:110px;top:28px;width:100px">Lorem ipsum dolor sit amet, consectetur adipiscing elit, sed do eiusmod tempor incididunt ut labore et dolore magna aliqua.<br><br><br>Lorem ipsum dolor sit amet, consectetur adipiscing elit, sed do eiusmod tempor incididunt ut labore et dolore magna aliqua.<br><br><br>Lorem ipsum dolor sit amet, consectetur adipiscing elit, sed do eiusmod tempor incididunt ut labore et dolore magna aliqua.</p>
  <div class="ft"></div><div class="url">www.keystoneharbor.com</div>
</section>

<section class="slide" style="left:486px;top:918px;width:226px;height:126px">
  <div class="hd"><span class="mark"></span><span class="rule"></span>Lorem Ipsum</div>
  <div style="position:absolute;left:22px;top:18px;width:50px;height:62px;background:#d6dbe2"></div>
  <p class="t" style="position:absolute;left:26px;top:32px;width:42px;text-align:center;color:var(--navy);font-size:4px">Lorem ipsum dolor sit amet, consectetur adipiscing elit</p>
  <div class="photo ph-people" role="img" aria-label="Business team celebrating success" style="left:72px;top:18px;width:144px;height:62px"></div>
  <div style="position:absolute;left:22px;top:84px;width:194px;display:flex;justify-content:space-around;text-align:center">
    <div><span class="mark" style="display:inline-block"></span><p class="t" style="width:50px">Lorem ipsum dolor sit amet, consectetur adipiscing elit, sed do eiusmod tempor.</p></div>
    <div><span class="mark" style="display:inline-block"></span><p class="t" style="width:50px">Lorem ipsum dolor sit amet, consectetur adipiscing elit, sed do eiusmod tempor.</p></div>
    <div><span class="mark" style="display:inline-block"></span><p class="t" style="width:50px">Lorem ipsum dolor sit amet, consectetur adipiscing elit, sed do eiusmod tempor.</p></div>
  </div>
  <div class="ft"></div><div class="url">www.keystoneharbor.com</div>
</section>

<section class="slide" style="left:722px;top:918px;width:226px;height:126px">
  <div class="hd"><span class="mark"></span><span class="rule"></span>Lorem Ipsum</div>
  <div style="position:absolute;left:0;top:18px;width:54px;height:100px;background:var(--navy)"></div>
  <p class="t w" style="position:absolute;left:6px;top:54px;width:44px">Lorem ipsum dolor sit amet, consectetur adipiscing elit, sed do eiusmod tempor incididunt ut labore et dolore magna aliqua.</p>
  <div class="photo ph-glass" role="img" aria-label="Glass office tower" style="left:54px;top:18px;width:56px;height:100px"></div>
  <div style="position:absolute;left:110px;top:18px;width:56px;height:100px;background:var(--navy)"></div>
  <p class="t w" style="position:absolute;left:116px;top:54px;width:44px">Lorem ipsum dolor sit amet, consectetur adipiscing elit, sed do eiusmod tempor incididunt ut labore et dolore magna aliqua.</p>
  <div class="photo ph-city" role="img" aria-label="Hand touching a digital interface" style="left:166px;top:18px;right:0;height:100px"></div>
  <div class="ft"></div><div class="url">www.keystoneharbor.com</div>
</section>

<section class="slide" style="left:960px;top:918px;width:230px;height:126px">
  <div class="hd"><span class="mark"></span><span class="rule"></span>Lorem Ipsum</div>
  <div style="position:absolute;left:0;top:18px;width:94px;height:100px;background:var(--navy);color:#fff;text-align:center">
    <div class="icon" style="margin:8px auto 6px;width:16px;height:16px"></div>
    <div class="icon" style="margin:0 auto 6px;width:16px;height:16px"></div>
    <p class="t w" style="width:60px;margin:0 auto">Lorem ipsum dolor sit amet, consectetur adipiscing elit.</p>
  </div>
  <div class="photo ph-rain" role="img" aria-label="Umbrella sheltering from rain" style="left:94px;top:18px;width:76px;height:100px"></div>
  <div style="position:absolute;left:174px;top:24px;width:52px">
    <p class="t" style="margin-bottom:6px">&#10003; Lorem ipsum dolor sit amet, consectetur adipiscing elit, sed do.</p>
    <p class="t" style="margin-bottom:6px">&#10003; Lorem ipsum dolor sit amet, consectetur adipiscing elit, sed do.</p>
    <p class="t">&#10003; Lorem ipsum dolor sit amet, consectetur adipiscing elit, sed do.</p>
  </div>
  <div class="ft"></div><div class="url">www.keystoneharbor.com</div>
</section>

<!-- Row 8 -->
<section class="slide" style="left:12px;top:1056px;width:226px;height:128px">
  <div class="hd"><span class="mark"></span><span class="rule"></span>Lorem Ipsum</div>
  <div class="photo ph-warm" role="img" aria-label="Family in a car" style="left:20px;top:22px;width:60px;height:92px"></div>
  <div style="position:absolute;left:84px;top:22px;width:44px;height:52px;background:var(--navy)"></div>
  <p class="t w" style="position:absolute;left:88px;top:34px;width:36px">Lorem ipsum dolor sit amet, consectetur adipiscing elit.</p>
  <div class="photo ph-warm" role="img" aria-label="Smiling family portrait" style="left:128px;top:22px;width:80px;height:52px"></div>
  <div style="position:absolute;left:84px;top:78px;width:124px;display:flex;justify-content:space-between;text-align:center">
    <div><span class="icon" style="width:10px;height:10px;color:var(--navy);margin:0 auto"></span><p class="t" style="width:38px;font-size:3px">Lorem ipsum dolor sit amet, consectetur adipiscing elit.</p></div>
    <div><span class="icon" style="width:10px;height:10px;color:var(--navy);margin:0 auto"></span><p class="t" style="width:38px;font-size:3px">Lorem ipsum dolor sit amet, consectetur adipiscing elit.</p></div>
    <div><span class="icon" style="width:10px;height:10px;color:var(--navy);margin:0 auto"></span><p class="t" style="width:38px;font-size:3px">Lorem ipsum dolor sit amet, consectetur adipiscing elit.</p></div>
  </div>
  <div class="ft"></div><div class="url">www.keystoneharbor.com</div>
</section>

<section class="slide" style="left:250px;top:1056px;width:224px;height:128px">
  <div class="hd"><span class="mark"></span><span class="rule"></span>Lorem Ipsum</div>
  <p class="t" style="position:absolute;left:28px;top:24px;width:42px">Lorem ipsum dolor sit amet, consectetur adipiscing elit, sed do eiusmod tempor incididunt ut labore et dolore magna aliqua.</p>
  <div class="photo ph-people" role="img" aria-label="Business handshake" style="left:72px;top:20px;width:124px;height:46px"></div>
  <div style="position:absolute;left:72px;top:60px;width:124px;background:var(--navy);color:#fff;font-size:4px;text-align:center;padding:1px">TITLE LOREM IPSUM</div>
  <div class="photo ph-city" role="img" aria-label="Businessman looking at the city" style="left:26px;top:70px;width:42px;height:44px"></div>
  <div style="position:absolute;left:26px;top:108px;width:42px;background:var(--navy);color:#fff;font-size:3.4px;text-align:center;padding:1px">TITLE LOREM IPSUM</div>
  <p class="t" style="position:absolute;left:76px;top:74px;width:122px">Lorem ipsum dolor sit amet, consectetur adipiscing elit, sed do eiusmod tempor incididunt ut labore et dolore magna aliqua.<br>Ut enim ad minim veniam, quis nostrud exercitation ullamco laboris nisi ut aliquip ex ea commodo consequat.<br>Duis aute irure dolor in reprehenderit in voluptate velit esse cillum dolore eu fugiat nulla pariatur.</p>
  <div class="ft"></div><div class="url">www.keystoneharbor.com</div>
</section>

<section class="slide" style="left:486px;top:1056px;width:226px;height:128px">
  <div class="hd"><span class="mark"></span><span class="rule"></span>Lorem Ipsum</div>
  <div class="photo ph-rain" role="img" aria-label="Businessman leaping over a gap" style="left:22px;top:20px;width:36px;height:40px"></div>
  <div style="position:absolute;left:58px;top:20px;width:34px;height:40px;background:#d6dbe2"></div>
  <p class="t" style="position:absolute;left:60px;top:34px;width:30px;color:var(--navy);font-size:3px">Lorem ipsum dolor sit amet, consectetur.</p>
  <div style="position:absolute;left:22px;top:60px;width:36px;height:54px;background:#d6dbe2"></div>
  <p class="t" style="position:absolute;left:24px;top:84px;width:32px;color:var(--navy);font-size:3px">Lorem ipsum dolor sit amet, consectetur.</p>
  <div class="photo ph-city" role="img" aria-label="Businessman pointing at a digital chart" style="left:58px;top:60px;width:84px;height:54px"></div>
  <div style="position:absolute;left:96px;top:20px;width:120px">
    <p class="t" style="margin-bottom:4px">&#10003; Lorem ipsum dolor sit amet, consectetur adipiscing elit, sed do eiusmod tempor incididunt ut labore et dolore.</p>
    <p class="t" style="margin-bottom:4px">&#10003; Ut enim ad minim veniam, quis nostrud exercitation ullamco laboris nisi ut aliquip ex ea commodo.</p>
    <p class="t">&#10003; Duis aute irure dolor in reprehenderit in voluptate velit esse cillum dolore eu fugiat nulla pariatur.</p>
  </div>
  <div class="ft"></div><div class="url">www.keystoneharbor.com</div>
</section>

<section class="slide" style="left:722px;top:1056px;width:226px;height:128px">
  <div class="hd"><span class="mark"></span><span class="rule"></span>Lorem Ipsum</div>
  <div class="photo ph-city" role="img" aria-label="Digital financial graph overlay" style="left:18px;top:20px;width:64px;height:48px"></div>
  <div style="position:absolute;left:82px;top:20px;width:56px;height:48px;background:#d6dbe2"></div>
  <div style="position:absolute;left:86px;top:24px;font-size:4px;color:var(--navy)">LOREM IPSUM</div>
  <p class="t" style="position:absolute;left:86px;top:30px;width:50px;font-size:3px">Lorem ipsum dolor sit amet, consectetur adipiscing elit, sed do eiusmod tempor incididunt.</p>
  <div class="photo ph-rain" role="img" aria-label="Rising chart arrow" style="left:138px;top:20px;width:68px;height:48px"></div>
  <div style="position:absolute;left:18px;top:68px;width:64px;height:46px;background:#d6dbe2"></div>
  <div style="position:absolute;left:22px;top:72px;font-size:4px;color:var(--navy)">LOREM IPSUM</div>
  <p class="t" style="position:absolute;left:22px;top:78px;width:56px;font-size:3px">Lorem ipsum dolor sit amet, consectetur adipiscing elit, sed do eiusmod tempor incididunt.</p>
  <div class="photo ph-glass" role="img" aria-label="Network of connected icons" style="left:82px;top:68px;width:56px;height:46px"></div>
  <div style="position:absolute;left:138px;top:68px;width:68px;height:46px;background:#d6dbe2"></div>
  <div style="position:absolute;left:142px;top:72px;font-size:4px;color:var(--navy)">LOREM IPSUM</div>
  <p class="t" style="position:absolute;left:142px;top:78px;width:60px;font-size:3px">Lorem ipsum dolor sit amet, consectetur adipiscing elit, sed do eiusmod tempor incididunt.</p>
  <div class="ft"></div><div class="url">www.keystoneharbor.com</div>
</section>

<section class="slide dark" style="left:960px;top:1056px;width:230px;height:128px">
  <div style="position:absolute;right:10px;top:14px;width:80px;height:80px;border:3px solid #2f5290"></div>
  <div style="position:absolute;left:28px;top:22px;font-size:11px">GET IN TOUCH</div>
  <div style="position:absolute;left:28px;top:46px;font-size:3.8px;line-height:1.4;color:#dbe3f0">
    <p style="margin-bottom:7px">&#9679; &nbsp;OUR OFFICES 400 Meridian Ave Ste 210,<br>&nbsp;&nbsp;&nbsp;&nbsp;Portland, Oregon 97204</p>
    <p style="margin-bottom:8px">&#9742; &nbsp;555-012-3456</p>
    <p style="margin-bottom:8px">&#9993; &nbsp;hello@keystoneharbor.com</p>
    <p>&#9675; &nbsp;www.keystoneharbor.com</p>
  </div>
</section>

</body>
</html>
```